Specialty Contact lens for children

We need a large size canvas 24x36" to advertise specialty fit contact lens for children to control myopia. please visit our website for more about our office theme www.tandriloo.com
We want modern , fresh, happy design. Color blue, green, white. Final design should communicate the best lens choice for the children. Banner to include a picture of happy teen playing sports or out in park without glasses. To portray the new ability to see without glasses.
ORTHO-K #1 MYOPIA control treatment for children
- Corrects your vision while you sleep
- Creates crisp clear vision all day
- Freedom: No glasses, No Surgery, No soft lenses
-Safe and effective for children and adults

Target Market(s)

8-25 years old

Industry/Entity Type

Health Care

Font styles to use
Sans Serif

Colors
0692cd
cee9f5
ecf7fb
ffffff
86cfc6

Requirements
Must have
• Picture of teen playing sports or outdoors without glasses
Nice to have
• office logo on banner. happy color blue, green, white.
• Modern font: century gothic

```html
<!DOCTYPE html>
<html lang="en">
<head>
<meta charset="UTF-8">
<title>Ortho-K Myopia Control – Lumaris Optometry</title>
<link rel="stylesheet" href="https://fonts.googleapis.com/css2?family=Montserrat:wght@600;800&family=Questrial&display=swap">
<style>
  :root {
    --brand-blue: #0692cd;
    --band-teal: #4cc3c9;
    --copy-teal: #3bb8bd;
    --accent-orange: #f07a22;
    --sky: #a8cdea;
    --grass: #8fc24a;
    --grass-soft: #c9e0a0;
    --white: #ffffff;
    --logo-gold: #8a8a8a;
    --line-teal: #86cfc6;
  }
  * { margin: 0; padding: 0; box-sizing: border-box; }
  html, body { width: 800px; height: 1200px; overflow: hidden; background: var(--white); }
  .poster {
    position: relative;
    width: 800px;
    height: 1200px;
    overflow: hidden;
    background: linear-gradient(to bottom, var(--grass) 0px, var(--grass) 430px, var(--grass-soft) 560px, #eef5df 700px, var(--white) 860px);
  }
  .hero-photo {
    position: absolute;
    left: 0; top: 0;
    width: 800px; height: 520px;
    background: linear-gradient(to bottom, var(--sky) 0%, #cfe3f1 22%, #7fb55a 34%, #9cc94f 60%, var(--grass) 100%);
    -webkit-mask-image: linear-gradient(to bottom, #000 80%, transparent 100%);
    mask-image: linear-gradient(to bottom, #000 80%, transparent 100%);
  }
  .deco-lines { position: absolute; left: 0; top: 0; width: 800px; height: 1200px; pointer-events: none; }
  .product-title {
    position: absolute;
    left: 40px; top: 402px;
    font-family: "Montserrat", sans-serif;
    font-weight: 600;
    font-size: 92px;
    line-height: 1;
    color: var(--white);
    letter-spacing: 1px;
  }
  .tagline-band {
    position: absolute;
    left: 42px; top: 506px;
    width: 716px; height: 46px;
    background: var(--band-teal);
    font-family: "Questrial", sans-serif;
    font-size: 32px;
    line-height: 46px;
    color: var(--white);
    padding-left: 14px;
  }
  .headline {
    position: absolute;
    left: 42px; top: 570px;
    font-family: "Montserrat", sans-serif;
    font-weight: 800;
    font-size: 49px;
    line-height: 62px;
    color: var(--brand-blue);
  }
  .headline .highlight { color: var(--accent-orange); display: block; }
  .benefits {
    position: absolute;
    left: 43px; top: 782px;
    list-style: none;
    font-family: "Questrial", sans-serif;
    font-size: 29px;
    line-height: 44px;
    color: var(--copy-teal);
  }
  .cta {
    position: absolute;
    left: 43px; top: 1130px;
    font-family: "Questrial", sans-serif;
    font-size: 26px;
    color: var(--brand-blue);
  }
  .practice-name {
    position: absolute;
    right: 42px; top: 1050px;
    width: 170px;
    text-align: center;
    font-family: "Questrial", sans-serif;
    color: var(--logo-gold);
  }
  .practice-name .mark {
    display: block;
    width: 60px; height: 60px;
    margin: 0 auto 14px;
    background: #f2c230;
  }
  .practice-name .name { display: block; font-size: 26px; line-height: 1; letter-spacing: 1px; }
  .practice-name .sub { display: block; font-size: 17px; line-height: 1.2; letter-spacing: 3px; }
</style>
</head>
<body>
  <main class="poster">
    <div class="hero-photo" role="img" aria-label="Photo of happy children running hand in hand through a sunny meadow of yellow dandelions, without glasses"></div>

    <svg class="deco-lines" viewBox="0 0 800 1200" aria-hidden="true">
      <line x1="0" y1="288" x2="430" y2="430" stroke="#ffffff" stroke-opacity="0.7" stroke-width="3"/>
      <line x1="0" y1="318" x2="380" y2="440" stroke="#ffffff" stroke-opacity="0.5" stroke-width="2"/>
      <line x1="0" y1="925" x2="520" y2="1100" stroke="#4cc3c9" stroke-width="4" stroke-opacity="0.8"/>
      <line x1="0" y1="955" x2="480" y2="1110" stroke="#86cfc6" stroke-width="2" stroke-opacity="0.6"/>
    </svg>

    <h1 class="product-title">ORTHO-K</h1>
    <p class="tagline-band">#1 myopia control treatment for children</p>

    <h2 class="headline">
      NO GLASSES, NO SURGERY,<br>NO DAYTIME LENSES.
      <span class="highlight">JUST GREAT VISION!</span>
    </h2>

    <ul class="benefits">
      <li>Help prevent nearsightedness from getting worse</li>
      <li>Corrects your vision while you sleep</li>
      <li>Safe and effective for both children and adults</li>
    </ul>

    <p class="cta">Get a free ORTHO-K Consultation today.</p>

    <div class="practice-name">
      <span class="mark"></span>
      <span class="name">LUMARIS</span>
      <span class="sub">OPTOMETRY</span>
    </div>
  </main>
</body>
</html>
```